BUsiness Card

We need a unique business card design for a new aesthetic practice, Meadowlark Aesthetics & Wellness, P.A. The reverse of the card should be an appointment card.

```html
<!DOCTYPE html>
<html lang="en">
<head>
<meta charset="utf-8">
<title>Meadowlark Aesthetics &amp; Wellness – Business &amp; Appointment Card</title>
<link rel="stylesheet" href="https://fonts.googleapis.com/css2?family=Open+Sans:wght@400;600&display=swap">
<style>
  :root {
    --navy: #0f4c6b;
    --teal: #1d9c98;
    --ink: #1f2a33;
    --paper: #ffffff;
    --box: #d9dcdf;
    --backdrop: #2b2d30;
  }
  * { box-sizing: border-box; margin: 0; padding: 0; }
  html, body { width: 1200px; height: 900px; overflow: hidden; }
  body {
    background: var(--backdrop);
    font-family: "Open Sans", Arial, sans-serif;
    color: var(--ink);
    position: relative;
  }
  .card {
    position: absolute;
    width: 600px;
    height: 343px;
    background: var(--paper);
    border-radius: 30px;
    overflow: hidden;
  }
  .card--appointment { left: 300px; top: 70px; }
  .card--contact { left: 300px; top: 487px; }

  .brand {
    position: absolute;
    display: flex;
    align-items: center;
    gap: 10px;
  }
  .brand__dot {
    width: 22px; height: 22px; border-radius: 50%;
    background: var(--navy);
    flex: none;
  }
  .brand__name {
    font-weight: 600;
    font-size: 19px;
    color: var(--navy);
    line-height: 1.15;
  }

  /* appointment side */
  .card--appointment .brand { left: 48px; top: 80px; width: 300px; }
  .appointment__band { position: absolute; right: 0; top: 0; width: 230px; height: 343px; }
  .appointment__title {
    position: absolute; left: 120px; top: 150px;
    font-size: 18px; color: var(--teal);
  }
  .appointment__form { position: absolute; left: 48px; top: 188px; width: 330px; font-size: 15px; }
  .form-row { display: flex; align-items: flex-end; gap: 8px; margin-bottom: 18px; }
  .form-line { flex: 1; border-bottom: 1.5px solid var(--navy); height: 18px; }
  .form-line--teal { border-color: var(--teal); }
  .form-label--teal { color: var(--teal); }
  .days { display: flex; gap: 14px; }
  .day { display: flex; align-items: center; gap: 5px; }
  .day__box { width: 13px; height: 11px; background: var(--box); }

  /* contact side */
  .card--contact .brand { right: 40px; top: 52px; }
  .person { position: absolute; left: 50px; top: 62px; }
  .person__name { font-size: 26px; font-weight: 600; color: var(--ink); }
  .person__title { font-size: 16px; color: var(--navy); }
  .person__rule { width: 60px; height: 2px; background: var(--navy); margin: 12px 0 0 18px; }
  .contact-list { position: absolute; left: 60px; top: 190px; list-style: none; font-size: 15px; }
  .contact-list li { display: flex; align-items: center; gap: 12px; margin-bottom: 7px; }
  .contact-list svg { width: 16px; height: 16px; fill: var(--navy); flex: none; }
  .contact__band {
    position: absolute; left: 0; bottom: 0; width: 600px; height: 70px;
    background: var(--navy);
    display: flex; align-items: center; padding-left: 70px;
  }
  .contact__web { color: #fff; font-size: 15px; letter-spacing: 3px; }
</style>
</head>
<body>

<section class="card card--appointment" aria-label="Appointment card">
  <svg class="appointment__band" viewBox="0 0 230 343" aria-hidden="true">
    <path d="M230 0 H40 Q110 30 130 90 L230 90 Z" fill="var(--navy)"/>
    <path d="M230 120 V343 H40 Q150 300 170 200 Q185 150 230 120 Z" fill="var(--navy)"/>
  </svg>
  <div class="brand">
    <span class="brand__name">Meadowlark Aesthetics &amp; Wellness</span>
  </div>
  <p class="appointment__title">Appointment</p>
  <div class="appointment__form">
    <div class="form-row"><span class="form-line"></span><span>has an appointment</span></div>
    <div class="form-row days">
      <span class="day">Mon<i class="day__box"></i></span>
      <span class="day">Tue<i class="day__box"></i></span>
      <span class="day">Wed<i class="day__box"></i></span>
      <span class="day">Thu<i class="day__box"></i></span>
      <span class="day">Fri<i class="day__box"></i></span>
    </div>
    <div class="form-row">
      <span class="form-label--teal">Date:</span><span class="form-line form-line--teal"></span>
      <span class="form-label--teal">Time:</span><span class="form-line form-line--teal"></span>
    </div>
  </div>
</section>

<section class="card card--contact" aria-label="Business card">
  <div class="brand">
    <span class="brand__dot"></span>
    <span class="brand__name">Meadowlark Aesthetics &amp; Wellness</span>
  </div>
  <div class="person">
    <p class="person__name">Your Name</p>
    <p class="person__title">Job Title</p>
    <div class="person__rule"></div>
  </div>
  <ul class="contact-list">
    <li><svg viewBox="0 0 16 16"><path d="M2 5 Q8 1 14 5 V7 H11 V5.5 H5 V7 H2 Z M4 8 H12 L13 13 H3 Z"/></svg>000 000 0000</li>
    <li><svg viewBox="0 0 16 16"><path d="M1 3 H15 V13 H1 Z M2 4 L8 9 L14 4 Z" fill-rule="evenodd"/></svg>youremail@xyz.com</li>
    <li><svg viewBox="0 0 16 16"><path d="M8 1 A5 5 0 0 1 13 6 C13 10 8 15 8 15 C8 15 3 10 3 6 A5 5 0 0 1 8 1 Z M8 4 A2 2 0 1 0 8 8 A2 2 0 1 0 8 4 Z" fill-rule="evenodd"/></svg>your adress</li>
  </ul>
  <div class="contact__band">
    <span class="contact__web">www.yourwebsite.com</span>
  </div>
</section>

</body>
</html>
```